Paw Pantry

We need a word press template designed for our new Word press site.
We'd like to mimic the design of the old site somewhat:
http://www.pawpantry.example/
to be ported over to the new site:
http://www.pawpantry.example/wp
We like the ornamental dog bone style in the old sites's banner/navigation. We may want to mimic that somewhat in the new design.
We have a retail store in historic Portsmouth, NH and we bake gourmet dog teats and sell leashes, collars, outdoor gear, beds, soft-sided crates, interactive toys and premium dog & cat foods.
Retail

```html
<!DOCTYPE html>
<html lang="en">
<head>
<meta charset="utf-8">
<title>Paw Pantry – Home</title>
<link rel="stylesheet" href="https://fonts.googleapis.com/css2?family=Arimo:wght@400;700&family=Carlito&family=PT+Sans:wght@400&family=PT+Sans+Narrow&family=Roboto+Condensed:wght@400&display=swap">
<style>
:root{
  --forest:#003300;
  --white:#ffffff;
  --red:#e8242c;
  --ink:#111111;
  --teal:#2aa3b7;
  --olive:#b2b630;
  --panel-top:#d0d0d0;
  --panel-bottom:#a2a2a2;
  --rule:#c8c8c8;
}
*{margin:0;padding:0;box-sizing:border-box}
html,body{width:1200px;height:1000px;overflow:hidden}
body{background:var(--forest);font-family:"Arimo",Arial,sans-serif;position:relative}
.top-band{position:absolute;left:0;top:55px;width:1200px;height:58px;background:var(--white);border-bottom:1px solid #222}
.brand{position:absolute;left:108px;top:16px;display:flex;align-items:center;gap:10px;z-index:3}
.brand-dot{width:26px;height:26px;border-radius:50%;background:var(--red)}
.brand-name{font-family:"Carlito",sans-serif;font-size:30px;color:var(--white)}
.search{position:absolute;left:910px;top:18px;width:187px;height:25px;background:var(--white);border:1px solid #999;border-radius:4px;display:flex;align-items:center}
.search-scope{width:38px;height:100%;border-right:1px solid #bbb;background:#eee;border-radius:4px 0 0 4px}
.search-field{flex:1;font-size:10px;color:#777;padding-left:4px}
.search-btn{width:22px;height:22px}
.main-nav{position:absolute;left:472px;top:55px;height:58px;display:flex;font-family:"Carlito",sans-serif;font-size:20.5px}
.main-nav a{color:var(--ink);text-decoration:none;padding:16px 10px 0;position:relative;height:100%}
.main-nav a+a::before{content:"";position:absolute;left:0;top:14px;height:31px;border-left:1px solid var(--rule)}
.main-nav a.current{color:var(--red);border-top:4px solid var(--red);padding:12px 9px 0 8px}
.hero{position:absolute;left:100px;top:113px;width:997px;height:513px;background:linear-gradient(100deg,#6f8a3a 0%,#b69a6a 22%,#c39a74 38%,#8c7a42 52%,#7c9c3c 66%,#a4c468 85%,#8fb55a 100%)}
.hero-caption{position:absolute;left:712px;top:131px;width:285px;height:189px;background:rgba(20,60,10,.85);color:var(--white);padding:28px 0 0 18px}
.hero-caption::before{content:"";position:absolute;left:0;top:29px;width:7px;height:52px;background:var(--red)}
.hero-caption h1{font-family:"PT Sans",sans-serif;font-weight:400;font-size:28px;letter-spacing:-.5px;line-height:1}
.hero-caption h2{font-family:"PT Sans",sans-serif;font-weight:400;font-size:16px;margin-top:5px}
.hero-caption p{font-family:"Roboto Condensed",sans-serif;font-size:11.5px;line-height:18px;margin-top:14px;width:265px}
.btn-more{display:inline-block;margin-top:16px;background:var(--red);color:var(--white);font-family:"Roboto Condensed",sans-serif;font-size:12px;padding:4px 11px;border-radius:12px}
.slider-arrows{position:absolute;right:5px;top:471px;display:flex;gap:3px}
.slider-arrows span{width:28px;height:35px;background:#222;display:flex;align-items:center;justify-content:center}
.content{position:absolute;left:100px;top:626px;width:997px;height:254px;background:var(--white)}
.news{position:absolute;left:14px;top:18px;width:591px;height:216px;background:linear-gradient(var(--panel-top),var(--panel-bottom))}
.news-head{display:flex;align-items:flex-end;height:38px}
.news-head h3{font-family:"PT Sans Narrow",sans-serif;font-weight:400;font-size:23px;letter-spacing:-.5px;padding:0 14px 2px 12px;border-right:1px solid #888;height:38px;width:151px;display:flex;align-items:flex-end}
.news-head a{font-size:10px;color:#222;margin:0 0 2px 12px;text-decoration:none}
.news-item{position:absolute;left:13px;display:flex}
.date{width:66px;height:66px;border-radius:50%;background:var(--forest);color:var(--white);text-align:center;flex:none}
.date b{display:block;font-size:28px;line-height:30px;margin-top:9px}
.date small{font-size:11px}
.news-item p{font-size:12px;line-height:18px;color:var(--ink);margin:3px 0 0 13px;width:480px}
.news-item strong{color:#d6252a}
.tile{position:absolute}
.tile-photo{left:618px;top:18px;width:366px;height:104px;background:linear-gradient(90deg,#5f8a2c,#9fc062 45%,#4f7f22)}
.tile-photo span{position:absolute;right:10px;top:8px;font-family:"PT Sans",sans-serif;font-size:18px;color:var(--white)}
.tile-about{left:618px;top:131px;width:179px;height:103px;background:var(--teal)}
.tile-contact{left:806px;top:131px;width:178px;height:103px;background:var(--olive)}
.tile svg{position:absolute;left:50%;top:8px;transform:translateX(-50%)}
.tile-label{position:absolute;left:0;bottom:0;width:100%;height:25px;background:rgba(0,0,0,.7);color:var(--white);font-family:"PT Sans",sans-serif;font-size:15px;text-align:center;line-height:25px}
.footer-copy{position:absolute;left:101px;top:908px;font-size:11px;color:var(--white)}
.footer-copy b{font-size:13px}
.social{position:absolute;right:116px;top:906px;display:flex;gap:12px;font-size:12px;color:var(--white)}
.social a{color:var(--white);text-decoration:none}
</style>
</head>
<body>
<div class="top-band"></div>
<div class="brand"><span class="brand-dot"></span><span class="brand-name">Paw Pantry</span></div>

<div class="search">
  <div class="search-scope"></div>
  <div class="search-field">Search</div>
  <svg class="search-btn" viewBox="0 0 22 22"><circle cx="9" cy="9" r="5" fill="none" stroke="#3b6ea8" stroke-width="2"/><line x1="13" y1="13" x2="18" y2="18" stroke="#3b6ea8" stroke-width="3"/></svg>
</div>

<nav class="main-nav">
  <a class="current" href="#">Home</a><a href="#">About Us</a><a href="#">Our Products</a><a href="#">Our Store</a><a href="#">Links</a><a href="#">News</a><a href="#">Contact Us</a>
</nav>

<section class="hero" role="img" aria-label="Two smiling women outdoors holding a small terrier, sunlit green foliage behind">
  <div class="hero-caption">
    <h1>Paw Pantry</h1>
    <h2>has been providing the Seacoast</h2>
    <p>Atqui numquam qui ut, eu pri illum evertitur contentiones. Diam affert ex his, sensibus persequeris liberavisse...</p>
    <span class="btn-more">learn more</span>
  </div>
  <div class="slider-arrows">
    <span><svg width="10" height="18" viewBox="0 0 10 18"><polyline points="8,1 2,9 8,17" fill="none" stroke="#fff" stroke-width="2"/></svg></span>
    <span><svg width="10" height="18" viewBox="0 0 10 18"><polyline points="2,1 8,9 2,17" fill="none" stroke="#fff" stroke-width="2"/></svg></span>
  </div>
</section>

<main class="content">
  <section class="news">
    <div class="news-head"><h3>news &amp; updates</h3><a href="#">view all »</a></div>
    <div class="news-item" style="top:58px">
      <div class="date"><b>10</b><small>MAY</small></div>
      <p><strong>Lorem ipsum dolor sit amet, consectetuer adipiscing elit,</strong><br>sed diam nonummy nibh euismod tincidunt ut laoreet dolore magna aliquam erat nonummy nibh euismod volutpat.</p>
    </div>
    <div class="news-item" style="top:129px">
      <div class="date"><b>29</b><small>JUNE</small></div>
      <p><strong>Duis autem vel eum iriure dolor in hendrerit in vulputate velit esse molestie consequat</strong> vel illum dolore eu feugiat nulla facilisis at vero eros et accumsan nonummy nibh euismod.</p>
    </div>
  </section>

  <div class="tile tile-photo" role="img" aria-label="Girl sitting with two terriers on grass"><span>photo &amp; video</span></div>
  <a class="tile tile-about" href="#">
    <svg width="64" height="64" viewBox="0 0 64 64"><circle cx="32" cy="32" r="31" fill="#000"/><circle cx="32" cy="16" r="5" fill="#fff"/><rect x="27" y="25" width="10" height="26" fill="#fff"/></svg>
    <span class="tile-label">about Us</span>
  </a>
  <a class="tile tile-contact" href="#">
    <svg width="66" height="62" viewBox="0 0 66 62"><polyline points="4,32 33,5 62,32" fill="none" stroke="#000" stroke-width="6"/><rect x="46" y="6" width="7" height="14" fill="#000"/><path d="M13 30 L33 12 L53 30 V60 H39 V42 H27 V60 H13 Z" fill="#000"/></svg>
    <span class="tile-label">contact Us</span>
  </a>
</main>

<footer>
  <p class="footer-copy">© Copyright 2013, all rights reserved with <b>Pawpantry</b></p>
  <nav class="social"><a href="#">Share</a><a href="#">Follow</a><a href="#">Connect</a></nav>
</footer>
</body>
</html>
```